Alternative Therapy Service Needs Compelling Brochure Design

Beyond the Meadow, LLC is looking for a brochure design that will capture the attention of others looking for support both mentally and physically. Colors that are soothing, convey support, growth, and strength are key!
The colors in my logo are great and a play or combo of any of those would be great....I am hoping the brochure can feel like an oasis from one's everyday life....I also love the tree concept of my logo as trees convey the growth and support that Beyond the Meadow offers...I am excited to see what you can create!

Hello All Designers! I am looking for a design on the outside and inside of the brochure...tri-fold or bi-fold brochures work! Please do not be concerned with adding text from my website into it as I am adding new services and will be updating the website ASAP I would like the brochure to be editable and easy to add and delete from as I change my business and add new elements and people to my staff... Thanks for all your contribution to my brochure project!

Reason: There are many designers who were invited later in the process and I would like to give them more time to design!

Industry/Entity Type

It Service

```html
<!DOCTYPE html>
<html lang="en">
<head>
<meta charset="utf-8">
<title>Beyond the Meadow — SomaSense &amp; Reiki Brochure</title>
<link href="https://fonts.googleapis.com/css2?family=Montserrat:wght@300;400;600;700&display=swap" rel="stylesheet">
<style>
  :root {
    --canvas: #c8ccd0;
    --paper: #ffffff;
    --royal: #3a5ba8;
    --sky-top: #2f86c8;
    --sky-bottom: #bfe0f2;
    --leaf: #8fc23f;
    --leaf-deep: #6ea52c;
    --leaf-light: #a6d05a;
    --ink: #4a4f55;
    --heading: #1f7fc4;
    --white: #ffffff;
  }
  * { box-sizing: border-box; margin: 0; padding: 0; }
  html, body { width: 1200px; height: 800px; overflow: hidden; }
  body {
    background: var(--canvas);
    font-family: "Montserrat", Arial, sans-serif;
    position: relative;
  }
  .brochure {
    position: absolute;
    left: 105px; top: 40px;
    width: 990px; height: 720px;
    display: flex;
    box-shadow: 0 6px 22px rgba(0,0,0,.18);
  }
  .panel { width: 330px; height: 720px; position: relative; overflow: hidden; }

  /* Inside panel */
  .panel--info { background: var(--paper); color: var(--ink); }
  .info-band {
    height: 16px;
    background: linear-gradient(90deg, #7cc0ea, var(--heading));
  }
  .info-body { padding: 18px 24px 0 24px; }
  .info-title {
    font-size: 21px; font-weight: 400; color: var(--heading);
    margin-bottom: 10px;
  }
  .info-body p { font-size: 9.4px; line-height: 1.42; margin-bottom: 6px; }
  .info-sub {
    font-size: 10px; font-weight: 700; color: var(--heading);
    margin: 10px 0 2px;
  }

  /* Back cover */
  .panel--contact {
    background: var(--royal); color: var(--white);
    text-align: center;
  }
  .brand-name {
    font-weight: 600; font-size: 19px;
    display: inline-flex; align-items: center; gap: 8px;
  }
  .brand-dot { width: 14px; height: 14px; border-radius: 50%; display: inline-block; }
  .panel--contact .brand { position: absolute; top: 170px; width: 100%; color: var(--leaf-light); }
  .panel--contact .brand-dot { background: var(--leaf-light); }
  .contact-title {
    position: absolute; top: 255px; width: 100%;
    font-weight: 300; font-size: 24px; line-height: 1.3;
  }
  .contact-address {
    position: absolute; top: 430px; width: 100%;
    font-size: 12.5px; line-height: 1.5;
  }
  .contact-lines {
    position: absolute; top: 510px; width: 100%;
    font-size: 12.5px; line-height: 1.5; font-weight: 300;
  }
  .contact-web {
    position: absolute; top: 600px; width: 100%;
    font-size: 14px; font-weight: 700;
  }

  /* Front cover */
  .panel--cover { background: var(--paper); }
  .cover-head {
    height: 135px; display: flex; align-items: center; justify-content: center;
    border-bottom: 3px solid var(--leaf);
  }
  .cover-head .brand { color: var(--leaf-deep); }
  .cover-head .brand-dot { background: var(--leaf-deep); }
  .cover-photo {
    height: 220px;
    background: linear-gradient(180deg, var(--sky-top), var(--sky-bottom) 80%, #d8ecc4);
  }
  .cover-field {
    height: 362px;
    background: linear-gradient(180deg, var(--leaf-deep), var(--leaf) 45%, var(--leaf-light));
    color: var(--white); text-align: center; position: relative;
  }
  .cover-title {
    padding-top: 40px;
    font-weight: 300; font-size: 42px; line-height: 1.2;
  }
  .cover-web {
    position: absolute; bottom: 42px; width: 100%;
    font-size: 15px; font-weight: 700;
  }
</style>
</head>
<body>
  <div class="brochure">
    <section class="panel panel--info">
      <div class="info-band"></div>
      <div class="info-body">
        <h2 class="info-title">How does SomaSense Work?</h2>
        <p>In a SomaSense session, a practitioner asks questions of the client's body to find out what area is a priority to address. A light tapping technique is used to help the brain balance and restore communication within the body.</p>
        <h3 class="info-sub">Asking the body</h3>
        <p>SomaSense asks the body which parts need better communication and harmony.</p>
        <h3 class="info-sub">Gentle tapping</h3>
        <p>Head: Tapping on the head tells the brain to be mindful and repair the communication. Heart: Tapping on the heart helps the body remember this dialogue.</p>
        <h3 class="info-sub">Prioritizing</h3>
        <p>In SomaSense, we respect the order of factors to be addressed, as determined by the body's innate wisdom.</p>
        <h3 class="info-sub">Integration</h3>
        <p>Once the body has been reminded of the issue, it can initiate its own healing processes. You body knows how to heal itself, it just needs to remember how.</p>
        <h3 class="info-sub">Tailored Just for You</h3>
        <p>A SomaSense session usually lasts between 15 and 60 minutes. The duration of a session is not indicative of the quality of the session or the results that occur. Because the client's innate wisdom is dictating the session, the client is assured of receiving exactly what they need at that particular time. During this time, the client is usually in a state of relaxation and is kept informed of the process. The client's innate wisdom will dictate when the session is complete and when to return.</p>
        <h3 class="info-sub">Background and Communication</h3>
        <p>The practitioner and client often begin by discussing the client's health and the issues they wish to address. Then, the client may relax in a chair or on a massage table while the practitioner uses neuromuscular biofeedback to establish a Yes/No communication between practitioner and client.</p>
        <h3 class="info-sub">Destinations and Details</h3>
        <p>The practitioner works up and down the SomaSense Protocol.</p>
      </div>
    </section>

    <section class="panel panel--contact">
      <div class="brand"><span class="brand-name"><span class="brand-dot"></span>Beyond the Meadow, LLC</span></div>
      <h2 class="contact-title">SomaSense<br>Reiki</h2>
      <address class="contact-address" style="font-style:normal">218 Willowbrook Road, Suite 40<br>Maple Grove, IL 60099 US</address>
      <div class="contact-lines">Phone: 555-014-2290<br>Email: hello@beyondthemeadow.center</div>
      <div class="contact-web">www.beyondthemeadow.center</div>
    </section>

    <section class="panel panel--cover">
      <header class="cover-head">
        <div class="brand"><span class="brand-name"><span class="brand-dot"></span>Beyond the Meadow, LLC</span></div>
      </header>
      <div class="cover-photo" role="img" aria-label="Photo of a joyful woman with arms raised against a clear blue sky"></div>
      <div class="cover-field">
        <h1 class="cover-title">SomaSense<br>Reiki</h1>
        <div class="cover-web">www.beyondthemeadow.center</div>
      </div>
    </section>
  </div>
</body>
</html>
```